Powerpoint Template needed for new Digital Consultancy

We have recently had our logo designed through Brushvale and would now like to extend the brand look & feel through to having a powerpoint template created that we can use as a master template within which to create our client presentations.
Typical slides required and in terms of what we would need templating is:

- Stylised header and footer for main content slides
- intro/front page slide
- contents page slide
- standardised font type and sizes, heading types (including sizes) for Level 1, Level 2 and Level 3 headings
- use of text colour and any standards/styling around when to use bold, underline, italics etc
- table styling for when we want to use tables in the presentation
- standards and styles around using bullet and number lists
- stylising use of imagery that is dropped in e.g. do all images have a certain border style or drop-shadow etc.
- style and slide layout/format for how team profiles are handled
- style and slide layout/format for how case studies are handled
- closing, contact-us page

We can send over logo files and colour/font styles etc used for the logo soon.

Target Market(s)

B2B professional clients that are either medium to large corporations or potentially some government departments.

Industry/Entity Type

Digital

Font styles to use
Sans Serif

Colors
ec1f27
f37122
f78f20
faa54b
f68d4d
0255a3

Requirements
Must have
• Ideally as many templated pages/master slide types as outlined above in the brief to meet the requirements of what the powerpoint deck will be used for. Namely client presentations and pitches.
• Versions of the logo are attached to give an idea of the colour palette and clean, modern style we are looking for, plus the type of font we are using and like.
• We are looking for the slide design to be modern, minimalistic, clean and not overuse of colour. Preferably a white slide background so it's easy to then read slide content when we populate the slides with text which will be in black.
Nice to have
• Not expecting to see too much more than simple use of the logo and a slide header perhaps using some sort of line as a break and then a simple footer as well.
• Consider using Abode font.
Should not have
• Too much block colour or elements that draw away from what will go in the main content body of our slides when we use them.

```html
<!DOCTYPE html>
<html lang="en">
<head>
<meta charset="utf-8">
<title>Lumenhalo Presentation Template</title>
<link rel="stylesheet" href="https://fonts.googleapis.com/css2?family=Open+Sans:ital,wght@0,300;0,400;0,600;0,700;1,400&display=swap">
<style>
  :root {
    --red: #ec1f27;
    --orange: #f37122;
    --amber: #f78f20;
    --light-orange: #faa54b;
    --blue: #0255a3;
    --ink: #333333;
    --grey: #6f6f6f;
    --rule: #d8d8d8;
    --band: #f4f4f4;
    --paper: #ffffff;
    --cream: #f3f1ef;
    --mint: #e3efe9;
    --divider: #000000;
  }
  * { box-sizing: border-box; margin: 0; padding: 0; }
  html, body { width: 1200px; height: 918px; overflow: hidden; background: var(--paper); }
  body { position: relative; font-family: "Open Sans", Arial, sans-serif; color: var(--ink); }

  .divider-v { position: absolute; left: 603px; top: 0; width: 1px; height: 918px; background: var(--divider); }
  .divider-h { position: absolute; left: 0; top: 449px; width: 1200px; height: 1px; background: var(--divider); }

  .slide { position: absolute; width: 597px; height: 449px; }
  .slide--content { left: 0; top: 0; }
  .slide--chart { left: 603px; top: 0; }
  .slide--team { left: 0; top: 449px; }
  .slide--closing { left: 607px; top: 516px; width: 593px; height: 334px; background: var(--red); }

  /* header */
  .header-mark { position: absolute; left: 14px; top: 76px; width: 20px; height: 60px; }
  .slide-title { position: absolute; left: 46px; top: 88px; font-size: 24px; font-weight: 300; color: var(--red); white-space: nowrap; }

  /* footer */
  .footer-rule { position: absolute; left: 22px; top: 354px; width: 470px; height: 12px; }
  .page-num { position: absolute; left: 16px; top: 354px; width: 12px; height: 12px; border-radius: 50%; background: var(--red); color: var(--paper); font-size: 6px; line-height: 12px; text-align: center; }
  .brand { position: absolute; left: 490px; top: 344px; display: flex; align-items: center; gap: 4px; }
  .brand-dot { width: 14px; height: 14px; border-radius: 50%; border: 2px solid var(--orange); }
  .brand-name { font-size: 17px; font-weight: 600; color: var(--orange); letter-spacing: -0.2px; }

  /* content slide */
  .feature-image { position: absolute; left: 41px; top: 143px; width: 256px; height: 213px; border: 4px solid var(--amber); background: linear-gradient(135deg, #0a1a33 0%, #123a6e 55%, #1f6fc0 80%, #0b1628 100%); }
  .feature-heading { position: absolute; left: 318px; top: 192px; font-size: 15px; font-weight: 400; color: var(--ink); }
  .feature-heading em { font-style: normal; color: var(--amber); }
  .feature-body { position: absolute; left: 318px; top: 216px; width: 240px; font-size: 11px; line-height: 15px; color: var(--grey); }

  /* chart slide */
  .chart-title { position: absolute; left: 672px; top: 146px; width: 206px; text-align: center; font-size: 10px; font-weight: 600; color: var(--amber); }
  .chart-note { position: absolute; font-size: 6.5px; line-height: 9px; font-style: italic; color: var(--grey); text-align: center; }
  .bar-chart { position: absolute; left: 672px; top: 162px; width: 206px; height: 160px; }
  .donut-chart { position: absolute; left: 948px; top: 172px; width: 150px; height: 145px; }
  .chart-legend { font-size: 5.5px; fill: var(--grey); font-family: "Open Sans", Arial, sans-serif; }

  /* team slide */
  .team-band { position: absolute; left: 0; top: 632px; width: 591px; height: 59px; background: var(--band); }
  .team-line { position: absolute; left: 121px; top: 664px; width: 349px; height: 1px; background: var(--rule); }
  .member { position: absolute; top: 620px; width: 120px; text-align: center; }
  .member-ring { width: 88px; height: 88px; margin: 0 auto; border-radius: 50%; border: 1px solid #f6c3a3; background: var(--paper); display: flex; align-items: center; justify-content: center; }
  .member-photo { width: 70px; height: 70px; border-radius: 50%; border: 5px solid var(--orange); background: linear-gradient(160deg, #ffffff 0%, #e9e9e9 100%); }
  .member-name { margin-top: 8px; font-size: 10px; font-weight: 700; color: var(--blue); }
  .member-role { margin: 1px auto 0; width: 70px; font-size: 6.5px; line-height: 8px; font-style: italic; color: var(--grey); }

  /* closing slide */
  .bubble { position: absolute; border-radius: 50%; }
  .bubble--main { left: 111px; top: 68px; width: 158px; height: 158px; background: var(--cream); display: flex; align-items: center; justify-content: center; font-size: 20px; color: var(--amber); }
  .bubble--mint { left: 201px; top: 177px; width: 28px; height: 28px; background: var(--mint); opacity: 0.85; }
  .bubble--small { left: 163px; top: 222px; width: 42px; height: 42px; background: var(--orange); }
  .bubble--large { left: 235px; top: 200px; width: 68px; height: 68px; background: var(--amber); }
  .contact { position: absolute; left: 332px; top: 72px; width: 200px; color: var(--paper); }
  .contact-title { font-size: 17px; font-weight: 400; margin-bottom: 8px; }
  .contact-row { display: flex; align-items: flex-start; gap: 6px; height: 25px; }
  .contact-icon { flex: 0 0 12px; width: 12px; height: 12px; margin-top: 1px; }
  .contact-text { font-size: 6.5px; line-height: 8px; width: 120px; }
  .closing-brand { position: absolute; left: 351px; top: 203px; width: 117px; height: 65px; background: var(--paper); display: flex; align-items: center; justify-content: center; gap: 4px; }
  .closing-brand .brand-name { color: var(--red); font-size: 19px; }
  .closing-brand .brand-dot { border-color: var(--red); }
</style>
</head>
<body>
  <div class="divider-v"></div>
  <div class="divider-h"></div>

  <!-- Content and image slide -->
  <section class="slide slide--content">
    <svg class="header-mark" viewBox="0 0 20 60"><line x1="10" y1="0" x2="10" y2="60" stroke="#cfcfcf" stroke-width="1"/><circle cx="7" cy="20" r="4.5" fill="none" stroke="#f37122" stroke-width="2"/></svg>
    <h1 class="slide-title">Content and Image Slide</h1>
    <div class="feature-image" role="img" aria-label="Photo of a business person touching a glowing blue growth chart"></div>
    <h2 class="feature-heading">Lorem <em>ipsum dolor</em></h2>
    <p class="feature-body">Lorem ipsum dolor sit amet, consectetur adipiscing elit. Etiam ornare velit at sem euismod, ut pellentesque odio sodales. Ut id rutrum lacus. Phasellus in laoreet dolor. Sed ac nunc fermentum, varius sem vitae, bibendum dui</p>
    <svg class="footer-rule" viewBox="0 0 470 12"><line x1="6" y1="6" x2="464" y2="6" stroke="#ec1f27" stroke-width="0.8"/><circle cx="464" cy="6" r="2.5" fill="#ec1f27"/></svg>
    <div class="page-num">9</div>
    <div class="brand"><span class="brand-dot"></span><span class="brand-name">lumenhalo</span></div>
  </section>

  <!-- Chart slide -->
  <section class="slide slide--chart">
    <svg class="header-mark" viewBox="0 0 20 60"><line x1="10" y1="0" x2="10" y2="60" stroke="#cfcfcf" stroke-width="1"/><circle cx="7" cy="20" r="4.5" fill="none" stroke="#f37122" stroke-width="2"/></svg>
    <h1 class="slide-title">Chart Slide</h1>
    <svg class="footer-rule" viewBox="0 0 470 12"><line x1="6" y1="6" x2="464" y2="6" stroke="#ec1f27" stroke-width="0.8"/><circle cx="464" cy="6" r="2.5" fill="#ec1f27"/></svg>
    <div class="page-num">10</div>
    <div class="brand"><span class="brand-dot"></span><span class="brand-name">lumenhalo</span></div>
  </section>

  <h2 class="chart-title">Lorem ipsum dolor sit amet</h2>
  <svg class="bar-chart" viewBox="0 0 206 160">
    <g stroke="#e6e6e6" stroke-width="0.6">
      <line x1="24" y1="20" x2="200" y2="20"/><line x1="24" y1="40" x2="200" y2="40"/><line x1="24" y1="60" x2="200" y2="60"/>
      <line x1="24" y1="80" x2="200" y2="80"/><line x1="24" y1="100" x2="200" y2="100"/><line x1="24" y1="120" x2="200" y2="120"/>
    </g>
    <g class="chart-legend" text-anchor="end">
      <text x="18" y="122">0</text><text x="18" y="102">1</text><text x="18" y="82">2</text>
      <text x="18" y="62">3</text><text x="18" y="42">4</text><text x="18" y="22">5</text>
    </g>
    <g>
      <rect x="32" y="34" width="7" height="86" fill="#ec1f27"/><rect x="42" y="72" width="7" height="48" fill="#f37122"/><rect x="52" y="80" width="7" height="40" fill="#f78f20"/>
      <rect x="76" y="70" width="7" height="50" fill="#ec1f27"/><rect x="86" y="32" width="7" height="88" fill="#f37122"/><rect x="96" y="80" width="7" height="40" fill="#f78f20"/>
      <rect x="120" y="50" width="7" height="70" fill="#ec1f27"/><rect x="130" y="84" width="7" height="36" fill="#f37122"/><rect x="140" y="60" width="7" height="60" fill="#f78f20"/>
      <rect x="164" y="30" width="7" height="90" fill="#ec1f27"/><rect x="174" y="64" width="7" height="56" fill="#f37122"/><rect x="184" y="20" width="7" height="100" fill="#f78f20"/>
    </g>
    <g class="chart-legend" text-anchor="middle">
      <text x="46" y="131">Category 1</text><text x="90" y="131">Category 2</text>
      <text x="134" y="131">Category 3</text><text x="178" y="131">Category 4</text>
    </g>
    <g class="chart-legend">
      <rect x="66" y="143" width="4" height="4" fill="#ec1f27"/><text x="72" y="147">Series 1</text>
      <rect x="96" y="143" width="4" height="4" fill="#f37122"/><text x="102" y="147">Series 2</text>
      <rect x="126" y="143" width="4" height="4" fill="#f78f20"/><text x="132" y="147">Series 3</text>
    </g>
  </svg>
  <p class="chart-note" style="left:662px; top:317px; width:226px;">Lorem ipsum dolor sit amet, consectetur adipiscing elit. Etiam ornare velit at sem euismod, ut pellentesque odio sodales.</p>

  <p class="chart-note" style="left:918px; top:146px; width:200px;">Lorem ipsum dolor sit amet, consectetur adipiscing elit. Etiam ornare velit at sem euismod, ut pellentesque odio sodales.</p>
  <svg class="donut-chart" viewBox="0 0 150 145">
    <text x="72" y="11" text-anchor="middle" font-size="9" fill="#f78f20" font-family="Open Sans, Arial, sans-serif">Sales</text>
    <g transform="rotate(-90 74 68)">
      <circle cx="74" cy="68" r="40" fill="none" stroke="#ec1f27" stroke-width="19" stroke-dasharray="170.9 251.3"/>
      <circle cx="74" cy="68" r="40" fill="none" stroke="#f37122" stroke-width="19" stroke-dasharray="0 170.9 55.3 251.3"/>
      <circle cx="74" cy="68" r="40" fill="none" stroke="#f78f20" stroke-width="19" stroke-dasharray="0 226.2 25.1 251.3"/>
    </g>
    <g class="chart-legend">
      <rect x="28" y="132" width="4" height="4" fill="#ec1f27"/><text x="34" y="136">1st Qtr</text>
      <rect x="60" y="132" width="4" height="4" fill="#f37122"/><text x="66" y="136">2nd Qtr</text>
      <rect x="94" y="132" width="4" height="4" fill="#f78f20"/><text x="100" y="136">3rd Qtr</text>
    </g>
  </svg>
  <p class="chart-note" style="left:918px; top:316px; width:200px;">Lorem ipsum dolor sit amet, consectetur adipiscing elit. Etiam ornare velit at sem euismod, ut pellentesque odio sodales.</p>

  <!-- Team slide -->
  <section class="slide slide--team">
    <svg class="header-mark" viewBox="0 0 20 60"><line x1="10" y1="0" x2="10" y2="60" stroke="#cfcfcf" stroke-width="1"/><circle cx="7" cy="20" r="4.5" fill="none" stroke="#f37122" stroke-width="2"/></svg>
    <h1 class="slide-title">Meet the Team</h1>
    <svg class="footer-rule" viewBox="0 0 470 12"><line x1="6" y1="6" x2="464" y2="6" stroke="#ec1f27" stroke-width="0.8"/><circle cx="464" cy="6" r="2.5" fill="#ec1f27"/></svg>
    <div class="page-num">11</div>
    <div class="brand"><span class="brand-dot"></span><span class="brand-name">lumenhalo</span></div>
  </section>
  <div class="team-band"></div>
  <div class="team-line"></div>
  <div class="member" style="left:61px;"><div class="member-ring"><div class="member-photo" role="img" aria-label="Team member portrait placeholder"></div></div><p class="member-name">Lorem Ipsum</p><p class="member-role">dolor sit amet consectetur adipiscing</p></div>
  <div class="member" style="left:234px;"><div class="member-ring"><div class="member-photo" role="img" aria-label="Team member portrait placeholder"></div></div><p class="member-name">Lorem Ipsum</p><p class="member-role">dolor sit amet consectetur adipiscing</p></div>
  <div class="member" style="left:410px;"><div class="member-ring"><div class="member-photo" role="img" aria-label="Team member portrait placeholder"></div></div><p class="member-name">Lorem Ipsum</p><p class="member-role">dolor sit amet consectetur adipiscing</p></div>

  <!-- Closing slide -->
  <section class="slide slide--closing">
    <div class="bubble bubble--main">Thank You</div>
    <div class="bubble bubble--mint"></div>
    <div class="bubble bubble--small"></div>
    <div class="bubble bubble--large"></div>
    <div class="contact">
      <h2 class="contact-title">Contact</h2>
      <div class="contact-row"><svg class="contact-icon" viewBox="0 0 12 12"><path d="M6 1 L11 6 H9.5 V11 H7 V8 H5 V11 H2.5 V6 H1 Z" fill="#ffffff"/></svg><p class="contact-text">Lorem ipsum dolor sit amet, consectetur adipiscing elit.</p></div>
      <div class="contact-row"><svg class="contact-icon" viewBox="0 0 12 12"><circle cx="6" cy="6" r="5" fill="#ffffff"/></svg><p class="contact-text">Lorem ipsum dolor sit amet, consectetur adipiscing elit.</p></div>
      <div class="contact-row"><svg class="contact-icon" viewBox="0 0 12 12"><circle cx="6" cy="6" r="5" fill="#ffffff"/></svg><p class="contact-text">Lorem ipsum dolor sit amet, consectetur adipiscing elit.</p></div>
      <div class="contact-row"><svg class="contact-icon" viewBox="0 0 12 12"><circle cx="6" cy="6" r="5" fill="#ffffff"/></svg><p class="contact-text">Lorem ipsum dolor sit amet, consectetur adipiscing elit.</p></div>
    </div>
    <div class="closing-brand"><span class="brand-dot"></span><span class="brand-name">lumenhalo</span></div>
  </section>
</body>
</html>
```